Harbor Stoneworks Business card logo

We are a tile and natural stone installation company with an emphasis on high quality and design assistance. I prefer a black background with a graphic logo or maybe a photo that gives a feel of tile/natural stone. I like bold, but tasteful colors. Something to really catch the eye without being gaudy. The final design should convey expert quality and attention to detail.

Contact Information for Business Card

HARBOR STONEWORKS Quality Design and Installation

Font styles to use
Other font styles liked:
• Graviton, Illegal curves

Requirements
Must have
• Business card must be an eye-catcher, but tasteful.
• Information I need on the card:
• Business name and tagline
• Neil Ashcombe, owner
• Phone: (xxx) xxx-xxxx
• Email
• Website

```html
<!DOCTYPE html>
<html lang="en">
<head>
<meta charset="utf-8">
<title>Harbor Stoneworks – Business Card</title>
<link rel="stylesheet" href="https://fonts.googleapis.com/css2?family=Questrial&display=swap">
<style>
  :root {
    --page: #ffffff;
    --stone-light: #c9bfae;
    --stone-mid: #a58a6f;
    --stone-warm: #8a6a52;
    --stone-dark: #3a3129;
    --shadow-band: #15120f;
    --brand-teal: #2fae8f;
    --text-white: #ffffff;
  }
  * { margin: 0; padding: 0; box-sizing: border-box; }
  html, body {
    width: 1200px;
    height: 712px;
    overflow: hidden;
    background: var(--page);
  }
  .card {
    position: relative;
    width: 1178px;
    height: 698px;
    overflow: hidden;
    font-family: "Questrial", "Century Gothic", sans-serif;
    color: var(--text-white);
  }
  .stone-photo {
    position: absolute;
    inset: 0;
    background:
      linear-gradient(180deg, var(--shadow-band) 0%, rgba(21,18,15,0) 5%, rgba(21,18,15,0) 93%, var(--shadow-band) 100%),
      radial-gradient(ellipse 60% 45% at 70% 55%, rgba(201,191,174,0.55), rgba(201,191,174,0) 70%),
      radial-gradient(ellipse 50% 40% at 25% 30%, rgba(165,138,111,0.7), rgba(165,138,111,0) 75%),
      linear-gradient(160deg, var(--stone-mid) 0%, var(--stone-light) 35%, var(--stone-warm) 65%, var(--stone-dark) 100%);
  }
  .brand-name {
    position: absolute;
    left: 290px;
    width: 710px;
    text-align: center;
    color: var(--brand-teal);
    line-height: 1;
    text-transform: uppercase;
  }
  .brand-name--top { top: 40px; font-size: 132px; letter-spacing: 6px; }
  .brand-name--bottom { top: 196px; font-size: 102px; letter-spacing: 2px; }
  .tagline {
    position: absolute;
    top: 332px;
    left: 286px;
    font-size: 46px;
    white-space: nowrap;
  }
  .website {
    position: absolute;
    top: 396px;
    left: 92px;
    font-size: 76px;
    white-space: nowrap;
  }
  .contact {
    position: absolute;
    left: 57px;
    top: 508px;
    list-style: none;
    font-size: 33px;
    line-height: 49px;
  }
  .contact li { white-space: nowrap; }
</style>
</head>
<body>
  <div class="card">
    <div class="stone-photo" role="img" aria-label="Close-up photograph of textured natural stone pavers in warm tan and grey tones"></div>

    <div class="brand-name brand-name--top">Harbor</div>
    <div class="brand-name brand-name--bottom">Stoneworks</div>

    <p class="tagline">Quality Design and Installation</p>
    <p class="website">www.harborstoneworks.com</p>

    <ul class="contact">
      <li>N: Neil Ashcombe</li>
      <li>P:&nbsp; 555-204-7811</li>
      <li>E: neil.a@harborstoneworks.com</li>
    </ul>
  </div>
</body>
</html>
```